Yard Sign Design Needed

Yard sign needed for mowing & landscaping company. Would like to use the top logo with black background which is attached. Would like MOWING to be in large standout letters. The word "landscaping" can be smaller and more artistic or omitted. Will need room for phone number once design is approved. The phone number will need to stand out and look identical/similar to the word 'MOWING"

```html
<!DOCTYPE html>
<html lang="en">
<head>
<meta charset="utf-8">
<title>Brinwood Contractors – Mowing Yard Sign</title>
<link href="https://fonts.googleapis.com/css2?family=Montserrat:wght@600;800&family=Big+Shoulders+Display:wght@500&display=swap" rel="stylesheet">
<style>
  :root {
    --ink: #000000;
    --edge: #2a2a2a;
    --lime: #9aaf14;
    --lime-bright: #b5c62a;
    --white: #ffffff;
  }
  html, body {
    margin: 0;
    padding: 0;
    width: 1200px;
    height: 1200px;
    overflow: hidden;
    background: var(--ink);
  }
  .sign {
    position: relative;
    width: 1200px;
    height: 1200px;
    box-sizing: border-box;
    border: 1px solid var(--edge);
    background: var(--ink);
    font-family: "Montserrat", sans-serif;
  }
  .sign-frame {
    position: absolute;
    left: 0;
    top: 0;
  }
  .brand {
    position: absolute;
    left: 0;
    right: 0;
    top: 215px;
    display: flex;
    align-items: center;
    justify-content: center;
    gap: 18px;
  }
  .brand-square {
    width: 46px;
    height: 46px;
    background: var(--lime);
  }
  .brand-name {
    margin: 0;
    font-family: "Montserrat", sans-serif;
    font-weight: 800;
    font-size: 40px;
    line-height: 1.1;
    letter-spacing: 2px;
    color: var(--lime);
    text-transform: uppercase;
  }
  .mower-strip {
    position: absolute;
    left: 112px;
    top: 390px;
    width: 960px;
    height: 166px;
    background: linear-gradient(180deg, rgba(181,198,42,0) 0%, rgba(181,198,42,0.35) 55%, var(--lime-bright) 78%, var(--lime) 100%);
    clip-path: polygon(0 100%, 0 76%, 14% 76%, 14% 0, 18% 0, 18% 76%, 100% 76%, 100% 100%);
  }
  .service-title {
    position: absolute;
    left: 0;
    right: 0;
    top: 578px;
    margin: 0;
    text-align: center;
    font-weight: 800;
    font-size: 208px;
    line-height: 1;
    letter-spacing: 2px;
    color: var(--lime);
  }
  .service-sub {
    position: absolute;
    left: 0;
    right: 0;
    top: 766px;
    margin: 0;
    text-align: center;
    font-family: "Big Shoulders Display", sans-serif;
    font-weight: 500;
    font-size: 90px;
    line-height: 1;
    letter-spacing: 5px;
    color: transparent;
    -webkit-text-stroke: 2px var(--white);
  }
  .divider {
    position: absolute;
    left: 127px;
    top: 940px;
    width: 950px;
    height: 2px;
    background: linear-gradient(90deg, var(--lime), var(--white));
  }
  .phone {
    position: absolute;
    left: 0;
    right: 0;
    top: 968px;
    margin: 0;
    text-align: center;
    font-weight: 800;
    font-size: 128px;
    line-height: 1;
    color: var(--lime);
  }
</style>
</head>
<body>
  <main class="sign">
    <svg class="sign-frame" width="1200" height="1200" viewBox="0 0 1200 1200" aria-hidden="true">
      <defs>
        <linearGradient id="frameStroke" x1="0" y1="0" x2="0" y2="1">
          <stop offset="0" stop-color="#ffffff"/>
          <stop offset="1" stop-color="#9aaf14"/>
        </linearGradient>
      </defs>
      <rect x="42" y="42" width="1116" height="1116" rx="56" ry="56" fill="none" stroke="url(#frameStroke)" stroke-width="3.5"/>
    </svg>

    <header class="brand">
      <span class="brand-square"></span>
      <p class="brand-name">Brinwood<br>Contractors LLC</p>
    </header>

    <div class="mower-strip" role="img" aria-label="Lawn mower silhouette cutting a long strip of green grass"></div>

    <h1 class="service-title">MOWING</h1>
    <p class="service-sub">LANDSCAPING</p>

    <div class="divider"></div>

    <p class="phone">Ph:00 000 000</p>
  </main>
</body>
</html>
```